Aviation Maintenance & Aircraft Cleaning Website

We need a fairly simple modern sleek website . Our company does aviation maintenance , aircraft cleaning , maintenance tracking . We work on KT420 HELICOPTERS , BELVANKO T82 HELICOPTERS , MORVELL TARRANT 512 HELICOPTERS. We would like a website that can be mobile as well with future ideas that an app where you could book cleanings and maintenance . Right now the biggest thing is for our customer to see a website , be able to book our services online and see our staff . the website must be modern and clean .

Target Market(s)

Aviation maintenance , aviation cleaning ,

Logo Text

TW but 1 image unlike the one i uploaded which is two . Im open for different aviation designs

Number of Pages Required

5+ page

Font styles to use
Serif

Requirements
Must have
• Home page , Aircraft Maintenance , Aircraft Cleaning , About Us , Contact , Careers

TW Aviation is insured and all of our mechanics are licensed by the NQB with an Airframe & Powerplant rating. ( FRONT PAGE )

Home page should have a simple nice picture of a KT420 or Belvanko T82 . My Logo as you can see seems like two logos . i would like 1 logo and made of the two if possible . (New ideas are welcome . )

Book a Cleaning Calendar should in the aircraft cleaning page . The aircraft cleaning page should have a picture of cleaning a helicopter or private jet .

Aircraft maintenance page should have a mechanic working on a helicopter . The Page should have a fast way to contact us .

We are a mobile AOG team who is available 24/7 . What we do
Scheduled & Unscheduled aircraft maintenance
Major & Minor repairs
STC installations
Aircraft Weight & Balance
Aircraft Painting
Aircraft Cleaning
Maintenance Tracking Utilizing Tracking Programs or spreadsheets
Removal & Installation of Components
Aircraft Pre Buy Inspections
Nice to have
• modern , sleek , aviation

Meet the Staff

Picture with Headset on flying in a helicopter

CEO Mateus Ferreira

Mateus Has been an aircraft mechanic for over 10 years . He has worked for the largest sightseeing & charter tourism company in the New York City area as well as repair stations & manufacturers. He has aircraft specific training to the Kestrane KT420 & Vornel 2K4. He has worked on several airframes including the Belvanko T82 and the Morvell 512. He has held every position in an aircraft maintenance department from mechanic up to Director of Maintenance . His work ethic and ability to manage mechanics in a organized and structured way gives any department or inspection a clear direction .

About Us

TW Aviation Services is company with aircraft maintenance experience . We focus on inspections of aircraft . Our Aircraft Mechanics who are pilots and IA's have experience many aircraft but specialize in the Kestrane KT420 , KT425 , KT435 . The Belvanko T82 and Morvell Tarrant 512 . Our focus is safety and to maintain aircraft day in and day out so our customer can operate the aircraft safely while keeping up with all the manufacturers inspections .

We know aircraft maintenance & maintenance planning . Leave the technical and tedious things to us . Get in your aircraft and fly knowing you have the best maintenance crew in the business.

```html
<!DOCTYPE html>
<html lang="en">
<head>
<meta charset="utf-8">
<title>TW Aviation – Contact</title>
<link href="https://fonts.googleapis.com/css2?family=Oswald:wght@500;600;700&family=Poppins:wght@400;500;600&display=swap" rel="stylesheet">
<style>
:root{
  --blue:#1a47a0;
  --ink:#1d1d1f;
  --muted:#666;
  --band:#e4e4e6;
  --slate:#6c6d72;
  --slate-dark:#5d5e63;
  --white:#fff;
  --map:#dcdcdc;
}
*{box-sizing:border-box;margin:0;padding:0}
html,body{width:1200px;height:2417px;overflow:hidden;background:var(--white);font-family:"Poppins",sans-serif;color:var(--ink)}
.page{position:relative;width:1200px;height:2417px}
.abs{position:absolute}
.display{font-family:"Oswald",sans-serif;font-weight:600;text-transform:uppercase;letter-spacing:-.5px}

/* header */
.site-header{position:absolute;top:0;left:0;width:1200px;height:87px;background:var(--white);z-index:3}
.brand{position:absolute;left:88px;top:22px;display:flex;align-items:center;gap:10px}
.brand-dot{width:36px;height:36px;border-radius:50%;background:var(--blue)}
.brand-name{font-family:"Oswald",sans-serif;font-weight:600;font-size:24px;color:var(--blue);white-space:nowrap}
.nav{position:absolute;right:90px;top:33px;display:flex;gap:28px;align-items:center;font-family:"Oswald",sans-serif;font-weight:500;font-size:16px;text-transform:uppercase;letter-spacing:-.3px}
.nav a{color:var(--ink);text-decoration:none}
.nav a.active{color:var(--blue)}

/* hero */
.hero-shape{position:absolute;top:0;left:0}
.hero-title{left:88px;top:232px;font-size:100px;color:var(--white);line-height:1}
.crumbs{left:88px;top:346px;font-size:26px;color:var(--white);word-spacing:6px}

/* contact */
.touch h2{font-size:44px;line-height:1}
.info{display:flex;gap:12px;margin-top:18px}
.info svg{flex:none;margin-top:4px}
.info h4{font-family:"Oswald",sans-serif;font-weight:600;font-size:18px;text-transform:uppercase;line-height:1.1}
.info p{font-size:15.5px;color:var(--muted);letter-spacing:.1px;white-space:nowrap}
.divider{width:460px;height:1px;background:#eee;margin:28px 0 16px 5px}
.social{display:flex;gap:10px;margin-top:40px}
.social span{width:34px;height:34px;border-radius:50%;box-shadow:0 6px 14px rgba(0,0,0,.15)}

.form{left:640px;top:627px;width:469px;height:490px;background:var(--blue);color:var(--white);padding:38px 37px}
.form h3{font-size:42px;line-height:1}
.form .lead{font-size:12.5px;margin-top:6px}
.field{margin-left:4px;border-bottom:1px solid rgba(255,255,255,.55);font-size:12.5px;font-weight:500;padding-bottom:11px;margin-top:22px}
.field.msg{height:76px;position:relative}
.send{position:absolute;right:37px;bottom:28px;font-size:15px;font-weight:600;letter-spacing:1px;border-bottom:2px solid var(--white);padding-bottom:2px}

/* map */
.map-frame{left:178px;top:1205px;width:846px;height:433px;background:var(--white);box-shadow:0 0 24px rgba(0,0,0,.06)}
.map{left:191px;top:1217px;width:818px;height:408px;background:var(--map)}
.bubble{left:466px;top:1400px;width:268px;height:108px;background:var(--white);border-radius:54px;text-align:center;padding-top:20px;box-shadow:0 4px 12px rgba(0,0,0,.08)}
.bubble h5{font-family:"Oswald",sans-serif;font-weight:600;font-size:18px}
.bubble p{font-size:12.5px;line-height:1.5;margin-top:4px}

/* footer */
.foot-shape{position:absolute;left:0;top:1700px}
.newsletter{left:0;width:1200px;top:1888px;text-align:center;color:var(--white);font-size:44px;line-height:1}
.subscribe{left:337px;top:1945px;width:520px;height:46px;display:flex}
.subscribe .input{flex:1;background:var(--white);display:flex;align-items:center;gap:10px;padding-left:22px;font-size:14.5px;color:#555}
.subscribe .btn{width:118px;background:var(--blue);color:var(--white);font-weight:600;font-size:14px;letter-spacing:.5px;display:flex;align-items:center;justify-content:center}
.foot-brand{left:132px;top:2095px;display:flex;align-items:center;gap:12px}
.foot-brand .brand-dot{width:56px;height:56px;background:var(--white)}
.foot-brand .brand-name{font-size:34px;color:var(--white)}
.col{top:2052px;color:var(--white)}
.col h6{font-family:"Oswald",sans-serif;font-weight:600;font-size:20px;text-transform:uppercase;letter-spacing:-.3px;margin-bottom:14px}
.col li{list-style:none;font-size:13.5px;line-height:28.5px;white-space:nowrap}
.col li::before{content:"›";margin-right:7px}
.contact-row{display:flex;gap:10px;font-size:15px;line-height:22.5px;margin-bottom:17px}
.contact-row svg{flex:none;margin-top:4px}
.bottom-bar{left:0;top:2333px;width:1200px;height:84px;background:var(--slate-dark);border-top:1px solid rgba(255,255,255,.1)}
.copy{left:0;width:1200px;top:2365px;text-align:center;color:var(--white);font-size:12.5px;font-weight:500}
.round{width:36px;height:36px;border-radius:50%;background:#66676c}
.to-top{left:1136px;top:2314px;width:36px;height:36px;border-radius:50%;background:var(--white);display:flex;align-items:center;justify-content:center;box-shadow:0 2px 8px rgba(0,0,0,.2)}
</style>
</head>
<body>
<div class="page">

<svg class="hero-shape" width="1200" height="620" viewBox="0 0 1200 620">
  <defs>
    <linearGradient id="photoTone" x1="0" y1="0" x2="1" y2="1">
      <stop offset="0" stop-color="#4a4f57"/>
      <stop offset=".5" stop-color="#2c2f36"/>
      <stop offset="1" stop-color="#6a6e76"/>
    </linearGradient>
  </defs>
  <path d="M0 87H1200V272C1000 420 700 600 300 603C150 604 40 560 0 520Z" fill="var(--band)"/>
  <path role="img" aria-label="Mechanic inspecting a helicopter engine with a flashlight" d="M0 87H1200V268C1000 400 700 560 330 570C170 574 50 520 0 400Z" fill="url(#photoTone)"/>
</svg>

<header class="site-header">
  <div class="brand"><span class="brand-dot"></span><span class="brand-name">TW Aviation</span></div>
  <nav class="nav">
    <svg width="18" height="16" viewBox="0 0 18 16"><path d="M9 0L0 8h2.5v8h5v-5h3v5h5V8H18z" fill="var(--ink)"/></svg>
    <a href="#">Aircraft Maintenance</a>
    <a href="#">Aircraft Cleaning</a>
    <a href="#">About Us</a>
    <a href="#" class="active">Contact</a>
    <a href="#">Careers</a>
  </nav>
</header>

<h1 class="abs display hero-title">Contact</h1>
<div class="abs display crumbs">Home &nbsp;|&nbsp; Contact</div>

<section class="abs touch" style="left:92px;top:660px;width:480px">
  <h2 class="display">Get in touch</h2>
  <div class="info">
    <svg width="16" height="16" viewBox="0 0 24 24"><path d="M6.6 10.8a15 15 0 006.6 6.6l2.2-2.2c.3-.3.7-.4 1-.2 1.1.4 2.3.6 3.6.6.6 0 1 .4 1 1V20c0 .6-.4 1-1 1A17 17 0 013 4c0-.6.4-1 1-1h3.5c.6 0 1 .4 1 1 0 1.3.2 2.5.6 3.6.1.3 0 .7-.2 1z" fill="#888"/></svg>
    <div><h4>Phone</h4><p>(+08) 123 456 7890</p></div>
  </div>
  <div class="info">
    <svg width="16" height="18" viewBox="0 0 24 24"><path d="M12 2a7 7 0 00-7 7c0 5 7 13 7 13s7-8 7-13a7 7 0 00-7-7zm0 9.5a2.5 2.5 0 110-5 2.5 2.5 0 010 5z" fill="#888"/></svg>
    <div><h4>Address</h4><p>Some address line goes here city name country name</p></div>
  </div>
  <div class="info">
    <svg width="18" height="16" viewBox="0 0 24 22"><path d="M6 0h12v6H6zM2 7h20a2 2 0 012 2v8h-5v5H5v-5H0V9a2 2 0 012-2zm5 8v5h10v-5z" fill="#888"/></svg>
    <div><h4>Fax</h4><p>(864) 123-456-789</p></div>
  </div>
  <div class="divider"></div>
  <div class="info">
    <svg width="16" height="16" viewBox="0 0 24 24"><path d="M6.6 10.8a15 15 0 006.6 6.6l2.2-2.2c.3-.3.7-.4 1-.2 1.1.4 2.3.6 3.6.6.6 0 1 .4 1 1V20c0 .6-.4 1-1 1A17 17 0 013 4c0-.6.4-1 1-1h3.5c.6 0 1 .4 1 1 0 1.3.2 2.5.6 3.6.1.3 0 .7-.2 1z" fill="#888"/></svg>
    <div><h4>Phone</h4><p>(+08) 123 456 7890</p></div>
  </div>
  <div class="info">
    <svg width="16" height="18" viewBox="0 0 24 24"><path d="M12 2a7 7 0 00-7 7c0 5 7 13 7 13s7-8 7-13a7 7 0 00-7-7zm0 9.5a2.5 2.5 0 110-5 2.5 2.5 0 010 5z" fill="#888"/></svg>
    <div><h4>Address</h4><p>Some address line goes here city name country name</p></div>
  </div>
  <div class="social">
    <span style="background:#2f4f9a"></span><span style="background:#2aa3e0"></span><span style="background:#d9342b"></span><span style="background:#a03fa8"></span><span style="background:#d0131a"></span>
  </div>
</section>

<section class="abs form">
  <h3 class="display">Reach to us</h3>
  <p class="lead">Contact us &amp; find how can benefit your company.</p>
  <div class="field">Enter your name...</div>
  <div class="field">Enter your Email..</div>
  <div class="field">Enter your Phone Number...</div>
  <div class="field">Enter your Subject...</div>
  <div class="field msg">Enter your Message...</div>
  <div class="send">SEND MESSAGE</div>
</section>

<div class="abs map-frame"></div>
<div class="abs map" role="img" aria-label="Street map of the office location"></div>
<svg class="abs" style="left:587px;top:1335px" width="28" height="40" viewBox="0 0 28 40"><path d="M14 0A14 14 0 000 14c0 10 14 26 14 26s14-16 14-26A14 14 0 0014 0z" fill="var(--blue)"/><circle cx="14" cy="14" r="4.5" fill="#fff"/></svg>
<div class="abs bubble"><h5>ADDRESS</h5><p>Some Address line goes here, city<br>name, country name here.</p></div>

<svg class="foot-shape" width="1200" height="717" viewBox="0 1700 1200 717">
  <path d="M880 1727C1060 1718 1180 1790 1200 1815V2000C1180 1880 1100 1760 950 1731Z" fill="var(--blue)"/>
  <path d="M0 2030C300 1900 700 1730 950 1728C1100 1730 1180 1840 1200 1900V2417H0Z" fill="var(--slate)"/>
</svg>

<h2 class="abs display newsletter">Newsletter</h2>
<div class="abs subscribe">
  <div class="input"><svg width="14" height="11" viewBox="0 0 14 11"><path d="M0 0h14v11H0zM1 1l6 5 6-5" fill="#999" stroke="#fff" stroke-width=".8"/></svg>Enter your email address</div>
  <div class="btn">SUBSCRIBE</div>
</div>

<div class="abs foot-brand"><span class="brand-dot"></span><span class="brand-name">TW Aviation</span></div>

<div class="abs col" style="left:431px">
  <h6>Quick Links</h6>
  <ul><li>Aircraft Maintenance</li><li>Aircraft Cleaning</li><li>About Us</li><li>Contact</li><li>Careers</li></ul>
</div>
<div class="abs col" style="left:642px">
  <h6>What We Do</h6>
  <ul><li>Major &amp; Minor repairs</li><li>STC installations</li><li>Aircraft Weight &amp; Balance</li><li>Aircraft Painting</li><li>Aircraft Cleaning</li></ul>
</div>
<div class="abs col" style="left:872px;width:220px">
  <h6>Contact Info</h6>
  <div class="contact-row"><svg width="14" height="11" viewBox="0 0 14 11"><path d="M0 0h14v11H0zM1 1l6 5 6-5" fill="#fff" stroke="var(--slate)" stroke-width=".8"/></svg><div>Email:<br>www.example.com</div></div>
  <div class="contact-row"><svg width="14" height="14" viewBox="0 0 24 24"><path d="M6.6 10.8a15 15 0 006.6 6.6l2.2-2.2c.3-.3.7-.4 1-.2 1.1.4 2.3.6 3.6.6.6 0 1 .4 1 1V20c0 .6-.4 1-1 1A17 17 0 013 4c0-.6.4-1 1-1h3.5c.6 0 1 .4 1 1 0 1.3.2 2.5.6 3.6.1.3 0 .7-.2 1z" fill="#fff"/></svg><div>Phone:<br>1 (+08) 123-456-78</div></div>
  <div class="contact-row"><svg width="14" height="16" viewBox="0 0 24 24"><path d="M12 2a7 7 0 00-7 7c0 5 7 13 7 13s7-8 7-13a7 7 0 00-7-7zm0 9.5a2.5 2.5 0 110-5 2.5 2.5 0 010 5z" fill="#fff"/></svg><div>Location:<br>Some address line goes here city name</div></div>
</div>

<div class="abs bottom-bar"></div>
<div class="abs copy">© 2020. ALL RIGHTS RESERVED</div>
<span class="abs round" style="left:917px;top:2357px"></span>
<span class="abs round" style="left:962px;top:2357px"></span>
<span class="abs round" style="left:1007px;top:2357px"></span>
<div class="abs to-top"><svg width="10" height="14" viewBox="0 0 10 14"><path d="M5 1v12M1 5l4-4 4 4" stroke="#333" stroke-width="1.3" fill="none"/></svg></div>

</div>
</body>
</html>
```